CARPET CLEANING FLYER WINDOW WASHING FLYER

Double Sided Flyer with TLVN Stamp in top corner
FLYER IS ALMOST COMPLETE......
Looking to enhance the layout and optimize the font

Would like to incorporate the van into the layout and make it look like it really fits in. I'd like to eliminate the white box I only need the TLVN stamp label

Use the silver metallic font everywhere that it looks good

Target Market(s)

residential home owners

Contact Information for Business Card

Design is almost complete, I will upload most recent version and label it

Font styles to use
Sans Serif

Colors
3277b5
ec1f27
00a990
9bcb3c
fece3e
a5d8ed
33a6d7

Requirements
Must have
• Remove the big white mailing label and only use TLVN Stamp
• On bottom of both sides remove/replace all contact info with logo uploaded today
• Keep logo/contact info to the bottom right (I want free space on left half of bottom)
• Replace FONT with SILVER FONT uploaded.... Change Color of Silver Font as Needed
• Integrate picture of van onto flyer
• On top of both sides reduce size of FREE ESTIMATES to 3/4 Current and justify left....

```html
<!DOCTYPE html>
<html lang="en">
<head>
<meta charset="utf-8">
<title>Harborline Cleaning &amp; Restoration – Double Sided Flyer</title>
<link rel="stylesheet" href="https://fonts.googleapis.com/css2?family=Archivo+Black&family=Open+Sans:ital,wght@0,400;0,600;0,700;0,800;1,700;1,800&family=Oswald:wght@500&family=Asap+Condensed:ital,wght@0,500;0,600;1,600&display=swap">
<style>
:root{
  --bg:#e9e9e9;
  --navy-deep:#172a6b;
  --navy:#1d3c8f;
  --blue:#3277b5;
  --blue-bright:#1f6fc4;
  --sky:#33a6d7;
  --sky-pale:#a5d8ed;
  --orange:#f3901f;
  --orange-light:#fbb34a;
  --red:#ec1f27;
  --green:#00a990;
  --lime:#9bcb3c;
  --yellow:#fece3e;
  --ink:#222;
  --white:#fff;
}
*{margin:0;padding:0;box-sizing:border-box}
html,body{width:968px;height:1200px;overflow:hidden;background:var(--bg)}
body{position:relative;font-family:"Open Sans",sans-serif}
.flyer{position:absolute;left:163px;width:618px;height:465px;overflow:hidden;
  background:linear-gradient(180deg,var(--blue-bright) 0%,var(--navy) 22%,var(--navy) 29%,var(--navy-deep) 30%,#1a3280 60%,var(--navy-deep) 100%);
  box-shadow:4px 6px 10px rgba(0,0,0,.35)}
.flyer--front{top:107px}
.flyer--back{top:612px}
.flyer::before{content:"";position:absolute;left:0;right:0;top:0;height:24px;
  background:linear-gradient(180deg,#2f7ad0,rgba(47,122,208,0))}
.pill{position:absolute;border-radius:18px;color:var(--white);font-weight:800;
  display:flex;align-items:center;justify-content:center;letter-spacing:-.3px;
  text-shadow:1px 1px 2px rgba(0,0,0,.45);border:2px solid rgba(255,255,255,.85)}
.pill--orange{background:linear-gradient(180deg,var(--orange-light),var(--orange) 55%,#e07a10);font-size:20px}
.pill--blue{background:linear-gradient(180deg,#3d93e3,var(--blue-bright) 55%,#1558a8);font-style:italic;font-size:21px}
.headline{position:absolute;font-family:"Archivo Black",sans-serif;line-height:1;white-space:nowrap;
  transform-origin:left top;
  background:linear-gradient(180deg,#fbfbfb 0%,#c9cdd2 40%,#7d838b 52%,#d9dde1 70%,#9aa0a7 100%);
  -webkit-background-clip:text;background-clip:text;color:transparent;
  filter:drop-shadow(2px 3px 2px rgba(0,0,0,.55))}
.headline--front{left:84px;top:52px;font-size:58px;letter-spacing:-1px;transform:scaleX(.8)}
.headline--back{left:15px;top:60px;font-size:46px;letter-spacing:-1px;transform:scaleX(.82)}
.seal{position:absolute;left:13px;top:101px;width:66px;height:66px;border-radius:50%;
  background:var(--sky);border:4px solid var(--white);box-shadow:0 0 0 3px var(--green)}
.grid{position:absolute;display:grid;border:2px solid var(--white);border-radius:8px;overflow:hidden;
  background:var(--white);gap:1px;box-shadow:0 3px 6px rgba(0,0,0,.4)}
.grid--front{left:25px;top:148px;width:563px;height:198px;grid-template-columns:repeat(3,1fr);grid-template-rows:repeat(2,1fr)}
.tile{position:relative;display:flex;align-items:flex-end;justify-content:center;padding-bottom:9px}
.tile__label{font-family:"Oswald",sans-serif;font-size:17px;color:var(--white);
  text-shadow:1px 1px 0 #000,0 0 4px rgba(0,0,0,.8)}
.photo--carpet{background:linear-gradient(135deg,#e6e2dc,#c9c0b4)}
.photo--window{background:linear-gradient(135deg,#c8d6e3,#3a6db0 70%,#9fb7cc)}
.photo--power{background:linear-gradient(135deg,#2a3050,#b06a5c 55%,#c88a78)}
.photo--water{background:linear-gradient(135deg,#7a4a2a,#b58a52 60%,#d07a3a)}
.photo--tile{background:linear-gradient(135deg,#7e7e7a,#a9a8a1 55%,#6c6c68)}
.photo--maint{background:linear-gradient(135deg,#e8c45a,#d9b992 40%,#2d3a6a)}
.photo--carpet2{background:linear-gradient(135deg,#f2f0ec,#cfcac0 60%,#2f5fb0)}
.photo--window2{background:linear-gradient(135deg,#a8b6c4,#5d7186 60%,#c7d2dc)}
.photo--power2{background:linear-gradient(135deg,#5b7a4a,#b2775e 55%,#9a8f86)}
.photo--tile2{background:linear-gradient(135deg,#b9a88e,#857358 55%,#2c5da8)}
.grid--back{left:25px;top:155px;width:567px;height:199px;grid-template-columns:repeat(6,1fr);grid-template-rows:repeat(2,1fr)}
.service{background:var(--white);padding:5px 3px 3px 6px;font-family:"Asap Condensed",sans-serif}
.service__title{color:var(--blue-bright);font-weight:500;font-size:17px;line-height:.98;margin-bottom:2px}
.service__text{font-family:"Open Sans",sans-serif;font-size:7.2px;line-height:1.35;color:var(--ink);font-weight:600;letter-spacing:-.2px}
.service__tag{font-style:italic;font-weight:600;color:var(--blue-bright);font-size:8.2px;line-height:1.2;margin-top:2px}
.stamp{position:absolute;left:516px;top:11px;width:80px;height:63px;background:var(--white);
  border:1.5px solid #000;font:700 8.3px/1.2 Arial,sans-serif;color:#000;text-align:center;
  display:flex;flex-direction:column;justify-content:center}
.stamp b{font-weight:800}
.van{position:absolute;left:392px;top:86px;width:202px;height:72px;border-radius:26px 30px 16px 14px;
  background:linear-gradient(180deg,#f4f6f9 0%,#c8d3e2 35%,#2c63b8 60%,#173f8c 100%);
  box-shadow:2px 4px 6px rgba(0,0,0,.45)}
.contact{position:absolute;left:336px;width:244px;text-align:right}
.contact--front{top:360px}
.contact--back{top:370px}
.contact__web{font:800 17px/1 "Open Sans",sans-serif;color:var(--orange);letter-spacing:.5px}
.contact__phone{font:800 italic 23px/1.1 "Open Sans",sans-serif;color:var(--white);margin-top:3px;
  text-shadow:1px 2px 2px rgba(0,0,0,.5)}
.brand{display:flex;align-items:center;justify-content:flex-end;gap:8px;margin-top:4px}
.brand__mark{width:32px;height:32px;border-radius:50%;background:var(--white);flex:none}
.brand__name{font:800 14px/1.1 "Open Sans",sans-serif;color:var(--white);text-align:left;white-space:nowrap}
</style>
</head>
<body>

<section class="flyer flyer--front" aria-label="Flyer front">
  <div class="pill pill--orange" style="left:160px;top:14px;width:296px;height:31px">Eco Friendly Cleaning!</div>
  <h1 class="headline headline--front">FREE ESTIMATES</h1>
  <div class="pill pill--blue" style="left:134px;top:118px;width:343px;height:34px">On ALL of Our Services!</div>
  <div class="grid grid--front">
    <div class="tile photo--carpet" role="img" aria-label="Child and puppy lying on a clean carpet"><span class="tile__label">Carpet Cleaning</span></div>
    <div class="tile photo--window" role="img" aria-label="Technician washing a window with a squeegee"><span class="tile__label">Window Washing</span></div>
    <div class="tile photo--power" role="img" aria-label="Pressure washer cleaning a patio"><span class="tile__label">Power Washing</span></div>
    <div class="tile photo--water" role="img" aria-label="Worker extracting water from a flooded floor"><span class="tile__label">Water Damage</span></div>
    <div class="tile photo--tile" role="img" aria-label="Tile floor being cleaned with a spinner tool"><span class="tile__label">Tile &amp; Grout</span></div>
    <div class="tile photo--maint" role="img" aria-label="Hard hat and tool belt in a home under repair"><span class="tile__label">Maintenance</span></div>
  </div>
  <div class="seal" aria-label="Certified products badge"></div>
  <div class="contact contact--front">
    <div class="contact__web">HARBORLINECLEAN.COM</div>
    <div class="contact__phone">555-014-2290</div>
    <div class="brand"><span class="brand__mark"></span><span class="brand__name">HARBORLINE<br>CLEANING &amp; RESTORATION</span></div>
  </div>
</section>

<section class="flyer flyer--back" aria-label="Flyer back">
  <div class="pill pill--orange" style="left:20px;top:13px;width:345px;height:32px">Eco Friendly Cleaning!</div>
  <h2 class="headline headline--back">FREE ESTIMATES</h2>
  <div class="pill pill--blue" style="left:60px;top:118px;width:282px;height:28px;font-size:19px">On ALL of Our Services!</div>
  <div class="stamp"><span>PRSRT STD</span><span>TLVN</span><span>U.S. POSTAGE</span><b>PAID</b><span>TLVN RETAIL</span></div>
  <div class="grid grid--back">
    <div class="photo--carpet2" role="img" aria-label="Technician steam cleaning carpet"></div>
    <div class="service"><div class="service__title">Carpet<br>Cleaning</div><div class="service__text">Safe Eco-Friendly Truck Mounted Steam Cleaning.</div><div class="service__tag">Say goodbye to those Ugly Carpet Stains.</div></div>
    <div class="photo--window2" role="img" aria-label="Technician on a ladder washing windows"></div>
    <div class="service"><div class="service__title">Window<br>Washing</div><div class="service__text">Interior/Exterior, Screens, tracks, frames &amp; sills..</div><div class="service__tag">Crystal Clear &amp; Streak Free Windows</div></div>
    <div class="photo--power2" role="img" aria-label="Pressure washing a garden walkway"></div>
    <div class="service"><div class="service__title">Power<br>Washing</div><div class="service__text">House washing safe for siding, drives, patios &amp; walks.</div><div class="service__tag">It's like an Instant Home Makeover</div></div>
    <div class="service"><div class="service__title">Water<br>Damage</div><div class="service__text">Got Mold or Water damage?</div><div class="service__tag">Free IR Imaging &amp; Leak Detection</div></div>
    <div class="photo--water" role="img" aria-label="Worker extracting water from a flooded floor"></div>
    <div class="service"><div class="service__title">Tile<br>&amp; Grout</div><div class="service__text">Clean, Restore &amp; Rejuvenate Tile, Grout &amp; Stone.</div><div class="service__tag">Renew Natural Luster</div></div>
    <div class="photo--tile2" role="img" aria-label="Cleaning a stone floor beside a sofa"></div>
    <div class="service"><div class="service__title">Maintenance<br>Services</div><div class="service__text">Paint, Patch, Repair, Replace.</div><div class="service__tag">YES! We can Fix It!</div></div>
    <div class="photo--maint" role="img" aria-label="Hard hat and tool belt in a home under repair"></div>
  </div>
  <div class="van" role="img" aria-label="Company service van with branded wrap"></div>
  <div class="contact contact--back">
    <div class="contact__web">HARBORLINECLEAN.COM</div>
    <div class="contact__phone">555-014-2290</div>
    <div class="brand"><span class="brand__mark"></span><span class="brand__name">HARBORLINE<br>CLEANING &amp; RESTORATION</span></div>
  </div>
</section>

</body>
</html>
```